Kelmora Legal Business Card

I require a corporate business card for a new legal services business.

I do not have a logo, nor do I want one.

I require a clean, neat a professional card for a law firm.

Details:

Business Name: Kelmora Legal
Name: Debra Lindqvist
Title: Corporate Services Manager
Location: Office 14 (Top Floor), Toravel Business Centre, Quinlan Grove Street, Alotau CBD, Milne Bay Province.
Postal Address: PO Box 593, Alotau, 211, Milne Bay Province, Papua New Guinea.
Contact: T: +675 6418250, F: +675 6413362, M: +675 72915867, E: dlindqvist@kelmoraexample.com.pg.

I look forward to your design submissions.

Industry/Entity Type

Legal

```html
<!DOCTYPE html>
<html lang="en">
<head>
<meta charset="utf-8">
<title>Kelmora Legal – Business Card</title>
<link href="https://fonts.googleapis.com/css2?family=Arimo:wght@400;700&family=Roboto+Slab:wght@700&display=swap" rel="stylesheet">
<style>
  :root {
    --backdrop: #1c1c17;
    --card-light: #f1effa;
    --card-lilac: #dcd8f0;
    --brand-blue: #1d12d6;
    --brand-blue-deep: #1206a8;
    --brand-navy: #120a9c;
    --accent-magenta: #ff1cc4;
    --accent-violet: #b21ee6;
    --ink: #111111;
    --white: #ffffff;
  }
  * { box-sizing: border-box; margin: 0; padding: 0; }
  html, body {
    width: 1200px; height: 900px; overflow: hidden;
    background: var(--backdrop);
  }
  .card {
    position: absolute; left: 70px; top: 130px;
    width: 1060px; height: 640px; overflow: hidden;
    background: linear-gradient(160deg, var(--white) 0%, var(--card-light) 45%, var(--card-lilac) 100%);
    font-family: "Arimo", Arial, sans-serif;
    color: var(--ink);
  }
  .card-art { position: absolute; inset: 0; }
  .holder {
    position: absolute; right: 70px; top: 62px; width: 380px;
    text-align: center;
  }
  .holder-name {
    font-size: 44px; color: var(--accent-magenta); font-weight: 400;
    letter-spacing: 0.5px; text-align: right;
  }
  .holder-rule {
    height: 2px; background: var(--white); width: 250px;
    margin: 8px 0 6px auto; margin-right: 40px;
  }
  .holder-title {
    font-size: 24px; color: var(--white); line-height: 27px;
    padding-left: 40px;
  }
  .brand {
    position: absolute; left: 62px; top: 228px;
    display: flex; align-items: center; gap: 24px;
  }
  .brand-dot {
    width: 104px; height: 104px; border-radius: 50%;
    background: var(--brand-blue);
  }
  .brand-name {
    font-family: "Roboto Slab", Georgia, serif; font-weight: 700;
    font-variant: small-caps; font-size: 64px; color: var(--brand-navy);
    letter-spacing: 2px; border-left: 2px solid var(--ink); padding-left: 18px;
    line-height: 84px;
  }
  .contacts { position: absolute; left: 74px; top: 375px; }
  .contact-row {
    display: flex; align-items: center; gap: 16px;
    font-size: 24px; line-height: 31px; margin-bottom: 26px;
  }
  .contact-icon { width: 28px; height: 28px; flex: none; }
  .label { color: var(--brand-blue); }
</style>
</head>
<body>
  <div class="card">
    <svg class="card-art" width="1060" height="640" viewBox="0 0 1060 640" aria-hidden="false">
      <defs>
        <linearGradient id="bandBlue" x1="0" y1="0" x2="1" y2="1">
          <stop offset="0" stop-color="var(--brand-blue-deep)"/>
          <stop offset="1" stop-color="var(--brand-blue)"/>
        </linearGradient>
        <linearGradient id="photoHaze" x1="0" y1="0" x2="1" y2="0">
          <stop offset="0" stop-color="#c9c5e2" stop-opacity="0"/>
          <stop offset="0.5" stop-color="#b9b5d6" stop-opacity="0.35"/>
          <stop offset="1" stop-color="#c9c5e2" stop-opacity="0"/>
        </linearGradient>
      </defs>
      <rect x="120" y="300" width="900" height="320" fill="url(#photoHaze)" role="img" aria-label="Soft background photograph of a judge's gavel"/>
      <path d="M0,0 H1060 V540 C930,360 640,70 0,66 Z" fill="url(#bandBlue)" role="img" aria-label="Blue band with faint scales of justice imagery"/>
      <path d="M0,78 C640,82 930,372 1060,556" fill="none" stroke="var(--accent-violet)" stroke-width="9"/>
      <path d="M0,76 C640,80 930,370 1060,553" fill="none" stroke="var(--accent-magenta)" stroke-width="3" opacity="0.8"/>
    </svg>

    <div class="holder">
      <div class="holder-name">Debra Lindqvist</div>
      <div class="holder-rule"></div>
      <div class="holder-title">Corporate Services<br>Manager</div>
    </div>

    <div class="brand">
      <div class="brand-dot"></div>
      <div class="brand-name">Kelmora Legal</div>
    </div>

    <div class="contacts">
      <div class="contact-row">
        <svg class="contact-icon" viewBox="0 0 28 28" aria-hidden="true">
          <rect width="28" height="28" rx="5" fill="var(--brand-blue)"/>
          <path d="M14 5a6 6 0 0 0-6 6c0 5 6 12 6 12s6-7 6-12a6 6 0 0 0-6-6zm0 8.5a2.5 2.5 0 1 1 0-5 2.5 2.5 0 0 1 0 5z" fill="var(--white)"/>
        </svg>
        <div>Office 14 (Top Floor), Toravel Business Centre,<br>Quinlan Grove Street, Alotau CBD, Milne Bay Province.</div>
      </div>
      <div class="contact-row">
        <svg class="contact-icon" viewBox="0 0 28 28" aria-hidden="true">
          <rect width="28" height="28" rx="5" fill="var(--brand-blue)"/>
          <rect x="6" y="9" width="16" height="11" rx="1" fill="none" stroke="var(--white)" stroke-width="2"/>
        </svg>
        <div>PO Box 593, Alotau, 211, Milne Bay Province, Papua New Guinea.</div>
      </div>
      <div class="contact-row">
        <svg class="contact-icon" viewBox="0 0 28 28" aria-hidden="true">
          <rect width="28" height="28" rx="5" fill="var(--brand-blue)"/>
          <path d="M7 11c0-3 14-3 14 0v2h-4v-2h-6v2H7z" fill="var(--white)"/>
          <rect x="8" y="14" width="12" height="7" rx="1.5" fill="var(--white)"/>
        </svg>
        <div><span class="label">T</span>: +675 6418250, <span class="label">F</span>: +675 6413362, <span class="label">M</span>: +675 72915867</div>
      </div>
      <div class="contact-row">
        <svg class="contact-icon" viewBox="0 0 28 28" aria-hidden="true">
          <rect width="28" height="28" rx="5" fill="var(--brand-blue)"/>
          <rect x="6" y="9" width="16" height="11" fill="none" stroke="var(--white)" stroke-width="2"/>
          <path d="M6 9l8 6 8-6" fill="none" stroke="var(--white)" stroke-width="2"/>
        </svg>
        <div>dlindqvist@kelmoraexample.com.pg.</div>
      </div>
    </div>
  </div>
</body>
</html>
```